Etiketten für Supplements
Zielgruppe
Verkauf von Supplements für einen gesunden Lifestyle
Aufgabenstellung
Grundlayout ist bei allen gleich
EU Richtlinien müssen nur eingehalten werden.
✅ Pflichtangaben auf einem Supplement-Etikett (EU-weit):
1. Verkehrsbezeichnung
z. B.: „Nahrungsergänzungsmittel mit Zink“
2. Nettofüllmenge
z. B.: „Inhalt: 90 Kapseln“
3. Verzehrempfehlung
z. B.: „Täglich 1 Kapsel mit ausreichend Flüssigkeit einnehmen.“ (unterschiedlich je nach Produkt erläutere ich unten weiter)
4. Zutatenliste (inkl. Kapselhülle & Zusatzstoffe)
Reihenfolge: mengenmäßig absteigend
5. Nährwerttabelle
Nährstoffangaben pro Tagesdosis
inkl. %NRV (Nutrient Reference Value, ehemals RDA)
6. Sicherheitshinweis
z. B.:
Nahrungsergänzungsmittel sind kein Ersatz für eine ausgewogene und abwechslungsreiche Ernährung sowie eine gesunde Lebensweise.
Die empfohlene tägliche Verzehrmenge darf nicht überschritten werden.
Außerhalb der Reichweite von kleinen Kindern aufbewahren.
7. Lagerhinweise
Trocken, verschlossen und vor Sonnenlicht geschützt lagern.
8. Mindesthaltbarkeitsdatum & LOT-Nr.
Mindestens haltbar bis: siehe Boden
LOT-Nr.: [Nummer]
9. Name und Adresse des Inverkehrbringers
Blue Orasent
Lindenhofweg 14
63118 Offenbach, Deutschland
Design wie es ungefähr aussehen sollte schicke ich im Anhang. Anzahl der Kapseln sollte stehen 90 Vegane Kapseln , dass es hochdosiert ist. Made in Germany 190x70mm sind die Maße. Ich habe auch im Anhang ein anderes geschickt es sollte professionell aussehen wie das.
Grundlayout beendet:
Produkt 1:
Magnesiumbiglyscinat:
???? 4 klare Benefits (EU-konform formuliert):
Trägt zur normalen Funktion des Nervensystems bei
Unterstützt eine normale Muskelfunktion
Hilft, Müdigkeit und Erschöpfung zu reduzieren
Trägt zur Erhaltung normaler Knochen und Zäh..

```html
<!DOCTYPE html>
<html lang="de">
<head>
<meta charset="utf-8">
<title>Blue Orasent – Vitamin C Etikett</title>
<link rel="stylesheet" href="https://fonts.googleapis.com/css2?family=Oswald:wght@400;500;600;700&family=Roboto:wght@400;700&family=Roboto+Condensed:wght@400;500&display=swap">
<style>
  :root{
    --stage:#3aa5a7;
    --label-top:#3fa5a2;
    --label-bottom:#6daf7b;
    --ink:#ffffff;
    --ink-soft:rgba(255,255,255,.92);
    --dark:#222428;
    --orange:#e5891f;
    --brand:#4c9a5e;
    --check:#3f9a52;
    --blob:#ffffff;
  }
  *{box-sizing:border-box;margin:0;padding:0}
  html,body{width:1200px;height:675px;overflow:hidden;background:var(--stage)}
  .label{
    position:absolute;left:50px;top:134px;width:1100px;height:406px;
    background:linear-gradient(180deg,var(--label-top) 0%,var(--label-bottom) 100%);
    font-family:"Roboto",Arial,sans-serif;color:var(--ink);
  }
  .col{position:absolute;font-size:11.4px;line-height:14.2px;color:var(--ink-soft)}
  .col h3{font-size:11.6px;font-weight:700;color:var(--ink);margin-bottom:1px}
  .col p{text-align:justify}
  .col section{margin-bottom:9px}
  .col-left{left:18px;top:18px;width:262px}
  .col-left .rule{border-top:1px solid rgba(255,255,255,.8);margin:6px 0 10px}
  .col-right{left:820px;top:18px;width:262px}
  .legal-name{text-align:justify;margin-bottom:10px}
  .legal-name b{color:var(--ink)}
  .nutrition{width:100%;border-collapse:collapse;font-size:9px;margin:4px 0 6px}
  .nutrition th{font-weight:700;text-align:left;padding:3px 0 5px;border-bottom:1px solid rgba(255,255,255,.8)}
  .nutrition td{padding:7px 0 7px;border-bottom:1px solid rgba(255,255,255,.8)}
  .nutrition .num{text-align:right}
  .nutrition .mid{text-align:center}
  .footnote{font-size:9.2px;line-height:12px;margin-bottom:14px}
  .leaf{position:absolute;background:radial-gradient(ellipse at center,rgba(255,255,255,.28),rgba(255,255,255,0) 70%);border-radius:50%}
  .leaf-left{left:300px;top:40px;width:90px;height:110px;transform:rotate(-30deg)}
  .leaf-left-low{left:278px;top:110px;width:70px;height:70px}
  .leaf-right{left:690px;top:35px;width:80px;height:110px;transform:rotate(25deg)}
  .blob{position:absolute;left:318px;top:18px;width:410px;height:330px}
  .center{position:absolute;left:318px;top:18px;width:410px;height:330px;text-align:center}
  .brand{position:absolute;left:0;right:0;top:48px;display:flex;flex-direction:column;align-items:center;gap:4px}
  .brand-dot{width:26px;height:26px;border-radius:50%;background:var(--brand)}
  .brand-name{font-family:"Oswald",sans-serif;font-weight:600;font-size:12px;letter-spacing:1px;color:var(--brand)}
  .title{position:absolute;left:0;right:0;top:114px;font-family:"Oswald",sans-serif;font-weight:700;font-size:58px;line-height:58px;letter-spacing:1px;color:var(--dark)}
  .title span{color:var(--orange)}
  .banner{position:absolute;left:75px;top:178px;width:268px;height:24px;background:var(--orange);color:#fff;font-family:"Oswald",sans-serif;font-weight:600;font-size:15px;line-height:24px;letter-spacing:.3px}
  .benefits{position:absolute;left:40px;right:30px;top:212px;list-style:none;font-family:"Roboto Condensed",sans-serif;font-size:9.6px;line-height:16.5px;color:var(--dark)}
  .benefits li{display:flex;justify-content:center;align-items:flex-start;gap:4px}
  .benefits svg{flex:none;margin-top:4px}
  .benefits .wrap{display:block;line-height:13px;padding-top:2px}
  .qty{position:absolute;left:318px;width:410px;top:364px;text-align:center;font-family:"Oswald",sans-serif;font-weight:500;font-size:15.5px;letter-spacing:.3px;color:var(--ink)}
  .origin{position:absolute;left:1027px;top:336px;width:54px;height:58px;border:2px solid #fff;border-radius:5px;background:#fff;display:flex;flex-direction:column;align-items:center;padding-top:5px}
  .flag{width:40px;height:26px;display:flex;flex-direction:column}
  .flag i{flex:1}
  .flag i:nth-child(1){background:#111}
  .flag i:nth-child(2){background:#d00}
  .flag i:nth-child(3){background:#f5c400}
  .origin span{font-family:"Roboto Condensed",sans-serif;font-weight:500;font-size:8.5px;line-height:9px;color:#333;text-align:center;margin-top:3px}
</style>
</head>
<body>
<div class="label">

  <div class="col col-left">
    <section>
      <h3>Verzehrempfehlung</h3>
      <p>Täglich 1 Kapsel mit ausreichend Wasser einnehmen, vorzugsweise zu einer Mahlzeit.</p>
    </section>
    <div class="rule"></div>
    <section>
      <h3>Zutaten</h3>
      <p>Calciumascorbat, Hydroxypropylmethylcellulose (Kapselhülle), Mikrokristalline Cellulose (Füllstoff)</p>
    </section>
    <section>
      <h3>Health Claims (EU-1924/2006)</h3>
      <p>Trägt zu einer normalen Funktion des Immunsystems bei.<br>Schützt die Zellen vor oxidativem Stress.<br>Trägt zur normalen Kollagenbildung bei – wichtig für Haut, Knochen, Zähne, Knorpel und Blutgefäße.<br>Hilft, Müdigkeit und Erschöpfung zu reduzieren.</p>
    </section>
    <section>
      <h3>Sicherheitshinweise</h3>
      <p>Nahrungsergänzungsmittel sind kein Ersatz für eine ausgewogene und abwechslungsreiche Ernährung sowie eine gesunde Lebensweise.<br>Die empfohlene tägliche Verzehrmenge darf nicht überschritten werden.<br>Außerhalb der Reichweite von kleinen Kindern aufbewahren.</p>
    </section>
  </div>

  <div class="leaf leaf-left" role="img" aria-label="Blattillustration"></div>
  <div class="leaf leaf-left-low" role="img" aria-label="Blattillustration"></div>
  <div class="leaf leaf-right" role="img" aria-label="Blattillustration"></div>

  <svg class="blob" viewBox="0 0 410 330" aria-hidden="true">
    <path d="M205 8 C300 4 392 40 402 140 C410 230 360 318 230 324 C120 330 20 300 10 200 C2 110 60 12 205 8 Z" fill="var(--blob)"/>
  </svg>

  <div class="center">
    <div class="brand">
      <div class="brand-dot"></div>
      <div class="brand-name">BLUE ORASENT</div>
    </div>
    <h1 class="title">VITAMIN <span>C</span></h1>
    <div class="banner">GEPUFFERTES CALCIUMASCORBAT</div>
    <ul class="benefits">
      <li><svg width="9" height="7" viewBox="0 0 9 7"><path d="M1 3.5 L3.5 6 L8 1" fill="none" stroke="var(--check)" stroke-width="1.8"/></svg>Trägt zu einer normalen Funktion des Immunsystems bei</li>
      <li><svg width="9" height="7" viewBox="0 0 9 7"><path d="M1 3.5 L3.5 6 L8 1" fill="none" stroke="var(--check)" stroke-width="1.8"/></svg>Trägt dazu bei, die Zellen vor oxidativem Stress zu schützen</li>
      <li><svg width="9" height="7" viewBox="0 0 9 7"><path d="M1 3.5 L3.5 6 L8 1" fill="none" stroke="var(--check)" stroke-width="1.8"/></svg>Trägt zur Verringerung von Müdigkeit und Ermüdung</li>
      <li><svg width="9" height="7" viewBox="0 0 9 7"><path d="M1 3.5 L3.5 6 L8 1" fill="none" stroke="var(--check)" stroke-width="1.8"/></svg><span class="wrap">Unterstützt die normale Kollagenbildung für Knochen, Knorpel,<br>Zähne, Zahnfleisch und Haut</span></li>
    </ul>
  </div>

  <div class="qty">90 VEGAN KAPSELN = 100G℮ - HOCHDOSIERT</div>

  <div class="col col-right">
    <p class="legal-name">Nahrungsergänzungsmittel mit <b>Vitamin C (Calciumascorbat)</b> – gepufferte, magenfreundliche Form</p>
    <h3>Nährwerttabelle (pro Tagesdosis = 1 Kapsel)</h3>
    <table class="nutrition">
      <tr><th>Nährstoff</th><th class="mid">Menge pro 1 Kapsel</th><th class="num">% NRV*</th></tr>
      <tr><td>Vitamin C</td><td class="mid">500 mg</td><td class="num">625%</td></tr>
    </table>
    <p class="footnote">* NRV = Nährstoffbezugswerte gemäß EU-Verordnung 1169/2011</p>
    <section>
      <h3>Lagerhinweise</h3>
      <p>Trocken, verschlossen und vor Sonnenlicht geschützt lagern.</p>
    </section>
    <section>
      <p>Mindestens haltbar bis: siehe Boden<br>LOT-Nr.: [Nummer]</p>
    </section>
    <section>
      <h3>Inverkehrbringer</h3>
      <p>[Name &amp; Adresse des Kunden]</p>
    </section>
  </div>

  <div class="origin">
    <div class="flag"><i></i><i></i><i></i></div>
    <span>MADE IN<br>GERMANY</span>
  </div>
</div>
</body>
</html>
```